Vexa Grease street sign

looking for a fresh new looking street sign .. sized 6ft tall 5ft wide <br/>"Vexa Grease<br/>The Performance Team"<br/>remove "... and Tune"<br/>remove "Quarn" the bottom should just read "The Performance Team"

Target Market(s)

motorist passing my location

Industry/Entity Type

Automotive

Font styles to use
Sans Serif

Requirements
Must have
• Vexa Grease
• The Performance Team
Should not have
• NO reference to "Quarn"

```html
<!DOCTYPE html>
<html lang="en">
<head>
<meta charset="utf-8">
<title>Vexa Grease – Street Sign</title>
<link rel="stylesheet" href="https://fonts.googleapis.com/css2?family=Anton&family=Roboto+Condensed:ital,wght@1,800&display=swap">
<style>
  :root {
    --page-bg: #5b5b5b;
    --night: #0c0a12;
    --ember: #3a1608;
    --streak-orange: #d2701c;
    --streak-blue: #3d5fb0;
    --streak-red: #b8231c;
    --name: #e9e9e9;
    --emblem-light: #8a8a8a;
    --emblem-dark: #2a2a2a;
    --paper: #f4f4f4;
  }
  html, body {
    margin: 0;
    padding: 0;
    width: 1200px;
    height: 2401px;
    overflow: hidden;
    background: var(--page-bg);
  }
  .sign {
    position: absolute;
    left: 100px;
    top: 600px;
    width: 1000px;
    height: 1200px;
    box-shadow: 0 10px 28px rgba(0,0,0,0.55);
  }
  .sign svg { display: block; width: 100%; height: 100%; }
  .brand-name { font-family: "Anton", "Oswald", sans-serif; font-weight: 400; }
  .tagline {
    font-family: "Roboto Condensed", "Arial Narrow", sans-serif;
    font-style: italic;
    font-weight: 800;
  }
</style>
</head>
<body>
<div class="sign">
  <svg viewBox="0 0 1000 1200" xmlns="http://www.w3.org/2000/svg">
    <defs>
      <linearGradient id="night-base" x1="0" y1="0" x2="0" y2="1">
        <stop offset="0" stop-color="var(--night)"/>
        <stop offset="0.55" stop-color="var(--ember)"/>
        <stop offset="0.75" stop-color="#140907"/>
        <stop offset="1" stop-color="#050505"/>
      </linearGradient>
      <linearGradient id="streaks" x1="0" y1="0" x2="1" y2="0.35">
        <stop offset="0" stop-color="var(--streak-blue)" stop-opacity="0.75"/>
        <stop offset="0.2" stop-color="var(--streak-orange)" stop-opacity="0.6"/>
        <stop offset="0.45" stop-color="var(--streak-red)" stop-opacity="0.25"/>
        <stop offset="1" stop-color="var(--night)" stop-opacity="0"/>
      </linearGradient>
      <radialGradient id="emblem-tone" cx="0.5" cy="0.5" r="0.6">
        <stop offset="0" stop-color="var(--emblem-light)" stop-opacity="0.85"/>
        <stop offset="1" stop-color="var(--emblem-dark)" stop-opacity="0.6"/>
      </radialGradient>
    </defs>

    <g class="backdrop" role="img" aria-label="Night road photo with long-exposure light streaks in orange, blue and red">
      <rect width="1000" height="1200" fill="url(#night-base)"/>
      <rect width="1000" height="1200" fill="url(#streaks)"/>
    </g>

    <g class="brand">
      <text class="brand-name" x="500" y="262" text-anchor="middle" font-size="190" textLength="770" lengthAdjust="spacing" fill="var(--name)">VEXA</text>
      <text class="brand-name" x="500" y="632" text-anchor="middle" font-size="330" textLength="770" lengthAdjust="spacingAndGlyphs" fill="var(--name)">GREASE</text>
    </g>

    <g class="emblem" role="img" aria-label="Racing emblem: crossed checkered flags over a banner">
      <rect x="85" y="690" width="835" height="270" rx="24" fill="url(#emblem-tone)"/>
    </g>

    <text class="tagline" x="500" y="1095" text-anchor="middle" font-size="72" textLength="760" lengthAdjust="spacingAndGlyphs" fill="var(--paper)">The Performance Team</text>
  </svg>
</div>
</body>
</html>
```